Mold remediation

Tri fold brochure explaining our mold remediation process

Target Market(s)

home owners that have water and mold damage

Industry/Entity Type

Restoration

Requirements
Must have
• Good design/clear message

```html
<!DOCTYPE html>
<html lang="en">
<head>
<meta charset="utf-8">
<title>Sound Frame Restoration – Mold Remediation Brochure</title>
<link href="https://fonts.googleapis.com/css2?family=Montserrat:wght@400;500;600;700;800;900&display=swap" rel="stylesheet">
<style>
  :root {
    --ink: #1f1f22;
    --charcoal: #2e2e33;
    --band: #333338;
    --panel-dark: #38383d;
    --paper: #ffffff;
    --paper-soft: #f1f1f2;
    --muted: #d9d9dc;
    --stage: #e4e4e6;
  }
  * { box-sizing: border-box; margin: 0; padding: 0; }
  html, body { width: 930px; height: 1200px; overflow: hidden; }
  body {
    background: var(--stage);
    font-family: "Montserrat", sans-serif;
    color: var(--ink);
    position: relative;
  }
  .spread {
    position: absolute;
    left: 30px;
    width: 870px;
    height: 555px;
    display: flex;
    box-shadow: 0 6px 18px rgba(0,0,0,.18);
  }
  .spread--outside { top: 30px; }
  .spread--inside { top: 615px; }
  .panel {
    position: relative;
    width: 290px;
    height: 100%;
    background: var(--paper);
    overflow: hidden;
  }
  .panel + .panel { border-left: 1px solid #e6e6e8; }
  .panel--soft { background: var(--paper-soft); }
  .panel--dark { background: var(--panel-dark); color: #fff; }
  .web-band {
    position: absolute;
    left: 0; right: 0; bottom: 0;
    height: 38px;
    background: var(--band);
    color: #fff;
    font-size: 11px;
    font-weight: 500;
    display: flex; align-items: center; justify-content: center;
    letter-spacing: .2px;
  }
  .web-band b { font-weight: 800; }
  .panel--dark .web-band { background: var(--charcoal); }
  .photo {
    position: absolute;
    display: block;
  }
  .bracket {
    position: absolute;
    border-top: 3px solid var(--ink);
    border-right: 3px solid var(--ink);
  }
  .bracket--low {
    border-top: none;
    border-bottom: 3px solid var(--ink);
    border-left: 3px solid var(--ink);
    border-right: none;
  }
  .panel--dark .bracket { border-color: #fff; }

  /* Back panel: services */
  .services { position: absolute; left: 24px; top: 330px; right: 20px; }
  .section-title {
    font-size: 15px; font-weight: 800;
    border-left: 3px solid var(--ink);
    padding-left: 7px; line-height: 1.1;
    margin-bottom: 8px;
  }
  .service-list { list-style: none; }
  .service-list li {
    display: flex; align-items: center; gap: 7px;
    font-size: 11.5px; font-weight: 500; line-height: 17px;
  }
  .service-list svg { flex: none; }
  .service-note { font-size: 8.5px; font-weight: 500; margin-top: 10px; }

  /* Middle panel: before/after + contact */
  .mark-square {
    position: absolute; left: 115px; top: 26px;
    width: 54px; height: 54px;
    border: 3px solid var(--ink);
    background: var(--paper);
  }
  .mark-name {
    position: absolute; left: 0; right: 0; top: 88px;
    text-align: center; font-size: 9px; font-weight: 700; letter-spacing: 1.5px;
  }
  .tag {
    position: absolute;
    background: var(--ink); color: #fff;
    font-size: 8px; font-weight: 700; letter-spacing: .6px;
    padding: 3px 9px;
  }
  .contact { position: absolute; left: 28px; top: 400px; right: 16px; }
  .contact .section-title { font-size: 10.5px; margin-bottom: 9px; }
  .contact-row {
    display: flex; gap: 9px; align-items: flex-start;
    font-size: 10.5px; font-weight: 500; line-height: 13px; margin-bottom: 7px;
  }
  .contact-row svg { flex: none; margin-top: 1px; }
  .contact-row b { font-weight: 800; }

  /* Cover */
  .brand {
    position: absolute; left: 26px; top: 26px;
    display: flex; align-items: center; gap: 10px;
  }
  .brand-square { width: 30px; height: 30px; background: var(--ink); }
  .brand-name { font-size: 17px; font-weight: 800; letter-spacing: 1.5px; line-height: 1; }
  .brand-sub { font-size: 6.5px; font-weight: 500; letter-spacing: 1px; margin-top: 3px; }
  .cover-title {
    position: absolute; left: 26px; right: 14px; top: 372px;
    font-size: 24px; font-weight: 900; line-height: 25px;
  }
  .license {
    position: absolute; left: 26px; top: 456px;
    font-size: 10px; font-weight: 500; display: flex; align-items: center; gap: 6px;
  }
  .license::before { content: ""; width: 8px; height: 8px; background: var(--ink); }

  /* Inside: steps */
  .step { position: absolute; left: 20px; right: 18px; }
  .step-tab {
    position: absolute; left: 0; top: 0;
    width: 24px; height: 78px;
    background: var(--ink); color: #fff;
    display: flex; align-items: center; justify-content: center;
  }
  .panel--dark .step-tab { background: #fff; color: var(--ink); }
  .step-tab span {
    transform: rotate(-90deg); white-space: nowrap;
    font-size: 13px; font-weight: 800;
  }
  .step-photo-wrap { position: absolute; left: 32px; top: 0; width: 180px; height: 78px; }
  .step-photo-wrap .photo { left: 0; top: 0; width: 172px; height: 78px; }
  .step-photo-wrap .bracket { left: 18px; top: -6px; width: 162px; height: 60px; }
  .step-body { position: absolute; left: 0; right: 0; top: 88px; }
  .step-heading {
    font-size: 11px; font-weight: 800; display: flex; align-items: center; gap: 6px;
    margin-bottom: 4px;
  }
  .step-heading::before { content: ""; width: 7px; height: 7px; background: currentColor; flex: none; }
  .step-text { font-size: 7.8px; line-height: 10.6px; font-weight: 500; }
  .step-text + .step-text { margin-top: 4px; }
  .intro-text { position: absolute; left: 20px; right: 18px; top: 22px; font-size: 7.8px; line-height: 10.6px; font-weight: 500; }
</style>
</head>
<body>

<!-- OUTSIDE SPREAD -->
<section class="spread spread--outside">

  <article class="panel panel--back">
    <div class="bracket" style="left:40px; top:14px; width:230px; height:300px;"></div>
    <div class="photo" role="img" aria-label="Crew framing a new wall on a residential job site" style="left:18px; top:26px; width:230px; height:138px; background:linear-gradient(160deg,#9cc1dc 0%,#b79a74 55%,#6d5a44 100%);"></div>
    <div class="photo" role="img" aria-label="Finished white kitchen with arched window and range" style="left:30px; top:170px; width:230px; height:138px; background:linear-gradient(180deg,#f4f2ee 0%,#e2ddd5 60%,#c9c2b8 100%);"></div>

    <div class="services">
      <h2 class="section-title">Services We Offer</h2>
      <ul class="service-list">
        <li><svg width="11" height="11" viewBox="0 0 12 12"><circle cx="6" cy="6" r="5" fill="none" stroke="#1f1f22" stroke-width="1.4"/><path d="M3.4 6.2l2 2 4.4-5" fill="none" stroke="#1f1f22" stroke-width="1.8"/></svg>Insurance Restoration</li>
        <li><svg width="11" height="11" viewBox="0 0 12 12"><circle cx="6" cy="6" r="5" fill="none" stroke="#1f1f22" stroke-width="1.4"/><path d="M3.4 6.2l2 2 4.4-5" fill="none" stroke="#1f1f22" stroke-width="1.8"/></svg>General Construction</li>
        <li><svg width="11" height="11" viewBox="0 0 12 12"><circle cx="6" cy="6" r="5" fill="none" stroke="#1f1f22" stroke-width="1.4"/><path d="M3.4 6.2l2 2 4.4-5" fill="none" stroke="#1f1f22" stroke-width="1.8"/></svg>Emergency Services</li>
        <li><svg width="11" height="11" viewBox="0 0 12 12"><circle cx="6" cy="6" r="5" fill="none" stroke="#1f1f22" stroke-width="1.4"/><path d="M3.4 6.2l2 2 4.4-5" fill="none" stroke="#1f1f22" stroke-width="1.8"/></svg>Mold Remediation</li>
        <li><svg width="11" height="11" viewBox="0 0 12 12"><circle cx="6" cy="6" r="5" fill="none" stroke="#1f1f22" stroke-width="1.4"/><path d="M3.4 6.2l2 2 4.4-5" fill="none" stroke="#1f1f22" stroke-width="1.8"/></svg>Water Damage Restoration</li>
        <li><svg width="11" height="11" viewBox="0 0 12 12"><circle cx="6" cy="6" r="5" fill="none" stroke="#1f1f22" stroke-width="1.4"/><path d="M3.4 6.2l2 2 4.4-5" fill="none" stroke="#1f1f22" stroke-width="1.8"/></svg>Smoke &amp; Fire Damage Restoration</li>
        <li><svg width="11" height="11" viewBox="0 0 12 12"><circle cx="6" cy="6" r="5" fill="none" stroke="#1f1f22" stroke-width="1.4"/><path d="M3.4 6.2l2 2 4.4-5" fill="none" stroke="#1f1f22" stroke-width="1.8"/></svg>Board-up, Temporary Shoring</li>
        <li><svg width="11" height="11" viewBox="0 0 12 12"><circle cx="6" cy="6" r="5" fill="none" stroke="#1f1f22" stroke-width="1.4"/><path d="M3.4 6.2l2 2 4.4-5" fill="none" stroke="#1f1f22" stroke-width="1.8"/></svg>Plumbing Repairs</li>
        <li><svg width="11" height="11" viewBox="0 0 12 12"><circle cx="6" cy="6" r="5" fill="none" stroke="#1f1f22" stroke-width="1.4"/><path d="M3.4 6.2l2 2 4.4-5" fill="none" stroke="#1f1f22" stroke-width="1.8"/></svg>Moisture Inspection</li>
      </ul>
      <p class="service-note">**Servicing all of LA County &amp; Ventura County</p>
    </div>
    <div class="web-band">www.<b>soundframerestoration</b>.com</div>
  </article>

  <article class="panel panel--soft panel--middle">
    <svg class="photo" style="left:0; top:0;" width="290" height="380" viewBox="0 0 290 380" aria-hidden="true">
      <polyline points="0,96 70,96 70,56 112,56" fill="none" stroke="#1f1f22" stroke-width="3"/>
      <polyline points="172,56 214,56 214,96 290,96" fill="none" stroke="#1f1f22" stroke-width="3"/>
      <polyline points="0,300 40,300 40,340 90,340" fill="none" stroke="#1f1f22" stroke-width="3"/>
    </svg>
    <div class="mark-square"></div>
    <div class="mark-name">SOUND FRAME</div>
    <div class="photo" role="img" aria-label="Bare kitchen before restoration" style="left:40px; top:118px; width:160px; height:120px; background:linear-gradient(170deg,#dcd6cc 0%,#b8ae9f 60%,#8d8374 100%);"></div>
    <div class="tag" style="left:118px; top:226px;">BEFORE</div>
    <div class="photo" role="img" aria-label="Restored kitchen with wood cabinets after restoration" style="left:90px; top:246px; width:160px; height:120px; background:linear-gradient(170deg,#c98a55 0%,#a4602f 55%,#6e3d1c 100%);"></div>
    <div class="tag" style="left:170px; top:354px;">AFTER</div>

    <div class="contact">
      <h2 class="section-title">CONTACT US:</h2>
      <div class="contact-row">
        <svg width="10" height="13" viewBox="0 0 10 13"><path d="M5 0C2.2 0 0 2.2 0 5c0 3.6 5 8 5 8s5-4.4 5-8c0-2.8-2.2-5-5-5zm0 7a2 2 0 110-4 2 2 0 010 4z" fill="#1f1f22"/></svg>
        <span>2140 W Linden Ave<br>#312 Glendale, CA 91203</span>
      </div>
      <div class="contact-row">
        <svg width="12" height="9" viewBox="0 0 12 9"><rect x=".5" y=".5" width="11" height="8" fill="#1f1f22"/><path d="M.8 1l5.2 4 5.2-4" fill="none" stroke="#fff" stroke-width="1"/></svg>
        <span>dana@soundframerestoration.com</span>
      </div>
      <div class="contact-row">
        <svg width="11" height="11" viewBox="0 0 12 12"><path d="M2.5 0.5l2 2.4-1.2 1.6c.8 1.6 2.2 3 3.8 3.8l1.6-1.2 2.4 2-1.3 2.4C5.3 11.2.8 6.7.5 2.3z" fill="#1f1f22"/></svg>
        <span><b>Call now</b> (818) 555-0147</span>
      </div>
    </div>
    <div class="web-band">www.<b>soundframerestoration</b>.com</div>
  </article>

  <article class="panel panel--cover">
    <div class="brand">
      <div class="brand-square"></div>
      <div>
        <div class="brand-name">SOUND FRAME</div>
        <div class="brand-sub">RESTORATION &amp; CONSTRUCTION CO., INC.</div>
      </div>
    </div>
    <div class="photo" role="img" aria-label="Two-storey home with company service truck parked in the driveway" style="left:0; top:86px; width:290px; height:262px; background:linear-gradient(180deg,#7fb2e2 0%,#c9d9e6 30%,#d9c69c 55%,#6f8a4f 78%,#bfb3a0 100%);"></div>
    <h1 class="cover-title">Fire, Water, Mold &amp; General Construction</h1>
    <p class="license">License # 480715</p>
    <div class="web-band">www.<b>soundframerestoration</b>.com</div>
  </article>
</section>

<!-- INSIDE SPREAD -->
<section class="spread spread--inside">

  <article class="panel">
    <div class="step" style="top:26px;">
      <div class="step-tab"><span>Step 1</span></div>
      <div class="step-photo-wrap">
        <div class="bracket"></div>
        <div class="photo" role="img" aria-label="Technician checking a ceiling with a moisture meter" style="background:linear-gradient(150deg,#8a7a63 0%,#5b4c3b 60%,#2f2820 100%);"></div>
      </div>
      <div class="step-body">
        <h3 class="step-heading">Inspection &amp; leak Assessment</h3>
        <p class="step-text">We will perform a thorough inspection &amp; determine the cause of loss. If the source cannot be determined we will expose the affected area (within containment) and perform a leak test.</p>
      </div>
    </div>
    <div class="step" style="top:184px;">
      <div class="step-tab"><span>Step 2</span></div>
      <div class="step-photo-wrap">
        <div class="bracket"></div>
        <div class="photo" role="img" aria-label="Plastic containment set up over a wood floor" style="background:linear-gradient(170deg,#d8d8da 0%,#b7aea2 55%,#8a5f3a 100%);"></div>
      </div>
      <div class="step-body">
        <h3 class="step-heading">Engineering Controls</h3>
        <p class="step-text">Proper engineering controls include things like containment and establishing and maintaining negative pressure using HEPA-filtered air filtration devices.</p>
        <p class="step-text">A containment is built using 6 mil fire retardant plastic, zipper door, decontamination chamber &amp; sometimes make up air to separate the affected areas with mold growth and water damage from the rest of the home or building. HEPA-filtered air filtration devices are used during controlled demolition and during detailed cleaning. Their purpose is to control and reduce contamination (spores, fungal fragments, mycotoxins, etc.)</p>
      </div>
    </div>
    <div class="web-band">www.<b>soundframerestoration</b>.com</div>
  </article>

  <article class="panel panel--dark">
    <div class="step" style="top:26px;">
      <div class="step-tab"><span>Step 3</span></div>
      <div class="step-photo-wrap">
        <div class="bracket"></div>
        <div class="photo" role="img" aria-label="Worker in protective suit removing damaged flooring" style="background:linear-gradient(170deg,#e0ddd6 0%,#b9ab93 55%,#7d6a50 100%);"></div>
      </div>
      <div class="step-body">
        <h3 class="step-heading">Controlled Demolition &amp; Removal</h3>
        <p class="step-text">Controlled demolition and removal is the critical time in which moldy and water-damaged building materials are removed or cleaned. Building materials that cannot be salvaged may include drywall, insulation, carpet, porous material, and sometimes wood. Materials should be removed a minimum of 18"-24" beyond what is visibly moldy. Building materials that can be saved (like solid wood &amp; structural components) require special attention such as HEPA vacuuming, damp wiping with antimicrobials, fungicidal, and the use of abrasive measures. Abrasive measures are critical to removing all parts of mold growth, including "roots" (hyphae &amp; mycelium structures) that may have grown into a material.</p>
      </div>
    </div>
    <div class="step" style="top:330px;">
      <div class="step-tab"><span>Step 4</span></div>
      <div class="step-photo-wrap">
        <div class="bracket"></div>
        <div class="photo" role="img" aria-label="Crew in protective suits cleaning a stripped room" style="background:linear-gradient(170deg,#d9d6d0 0%,#a8a092 55%,#6f6656 100%);"></div>
      </div>
      <div class="step-body">
        <h3 class="step-heading">Detailed Cleaning</h3>
        <p class="step-text">Detailed cleaning, sometimes known as small particle cleaning, is the last and one of the most important parts of the remediation process. Every square inch inside the containment is meticulously cleaned through a very strategic and labor-intensive process.</p>
      </div>
    </div>
    <div class="web-band">www.<b>soundframerestoration</b>.com</div>
  </article>

  <article class="panel">
    <p class="intro-text">This is often the most time-consuming and expensive part of the whole process. All surfaces are cleaned (ceilings, walls, floors, plastic sheeting, etc.) We HEPA vacuum, damp wipe with an antimicrobial/fungicidal and microfiber cloths, then HEPA vacuum again.</p>
    <div class="step" style="top:100px;">
      <div class="step-tab"><span>Step 5</span></div>
      <div class="step-photo-wrap">
        <div class="bracket"></div>
        <div class="photo" role="img" aria-label="Gloved hand holding a mold culture dish" style="background:linear-gradient(160deg,#e9ecef 0%,#a9b4bd 55%,#5f6a73 100%);"></div>
      </div>
      <div class="step-body">
        <h3 class="step-heading">Mold clearance test</h3>
        <p class="step-text">Also known as post clearance testing, is an important part of determining if remediation was successful at a microscopic level. It is also important to confirm with a moisture meter that buildings materials are dry prior to rebuild. After we have achieved a "pass" we can then remove equipment &amp; containment chambers.</p>
      </div>
    </div>
    <div class="step" style="top:302px;">
      <div class="step-tab"><span>Step 6</span></div>
      <div class="step-photo-wrap">
        <div class="bracket"></div>
        <div class="photo" role="img" aria-label="Renovated bathroom with grey tile and round mirror" style="background:linear-gradient(170deg,#cfcfd1 0%,#9c9ca0 55%,#5d5d62 100%);"></div>
      </div>
      <div class="step-body">
        <h3 class="step-heading">Repairs &amp; Construction</h3>
        <p class="step-text">Our restoration &amp; construction team manages the entire rebuild process, including pack out of personal property &amp; any improvements and modifications you wish to make. With precise attention to detail, we'll quickly proceed with reconstruction until your home is completely restored.</p>
      </div>
    </div>
    <div class="web-band">www.<b>soundframerestoration</b>.com</div>
  </article>
</section>

</body>
</html>
```